Business Cards and Stationery for Brook Harlow Supply & Advisory sàrl
Simple
Karim Ait Lounes
Associé gérant
CP 7148
CH-1002 Lausanne
Switzerland
kal@brookharlow.ch
www.brookharlow.ch
Business cards to look fresh, in alignment with logo branding.
Colour scheme, images and writting to coordinate with logo.
We may soon need to change our office address and, possibly add phone and fax numbers, so we need to use a font that I can modify.
We want to use the logo designed through Tessavane.

```html
<!DOCTYPE html>
<html lang="fr">
<head>
<meta charset="utf-8">
<title>Brook Harlow Supply &amp; Advisory sàrl – Business Card</title>
<link rel="stylesheet" href="https://fonts.googleapis.com/css2?family=Open+Sans:wght@400;600;700&display=swap">
<style>
  :root {
    --bg: #e4e4e2;
    --card-front: #ffffff;
    --card-back: #4a4a4a;
    --green-lime: #8dc63f;
    --green-deep: #34a853;
    --text-grey: #6d6d6d;
    --text-white: #ffffff;
    --shadow: rgba(0,0,0,0.18);
  }
  * { margin: 0; padding: 0; box-sizing: border-box; }
  html, body { width: 1200px; height: 901px; overflow: hidden; }
  body {
    background: var(--bg);
    font-family: "Open Sans", Arial, sans-serif;
    position: relative;
  }
  .card {
    position: absolute;
    width: 540px;
    height: 310px;
    border-radius: 14px;
    box-shadow: 0 10px 24px var(--shadow);
    overflow: hidden;
  }
  .card-front { left: 40px; top: 295px; background: var(--card-front); }
  .card-back  { left: 620px; top: 295px; background: var(--card-back); }

  .brand {
    position: absolute;
    display: flex;
    align-items: center;
    gap: 10px;
  }
  .brand-dot {
    width: 34px; height: 34px; border-radius: 50%;
    background: var(--green-deep);
    flex: none;
  }
  .brand-name {
    font-weight: 700;
    color: var(--green-lime);
    line-height: 1.15;
  }
  .card-front .brand { left: 34px; top: 160px; }
  .card-front .brand-name { font-size: 17px; width: 190px; }

  .contact { position: absolute; left: 290px; top: 42px; }
  .contact-name {
    font-size: 21px; font-weight: 600; color: var(--green-lime);
  }
  .contact-role {
    font-size: 11px; color: var(--text-grey); margin-bottom: 24px;
  }
  .contact-line {
    display: flex; align-items: flex-start; gap: 8px;
    font-size: 11px; line-height: 1.35; color: var(--text-grey); margin-bottom: 6px;
  }
  .contact-line svg { width: 11px; height: 11px; flex: none; margin-top: 2px; }

  .card-back .brand { right: 36px; top: 150px; }
  .card-back .brand-name { font-size: 20px; color: var(--text-white); width: 220px; }
</style>
</head>
<body>

<section class="card card-front" aria-label="Business card front">
  <div class="brand">
    <span class="brand-dot"></span>
    <span class="brand-name">Brook Harlow Supply &amp; Advisory sàrl</span>
  </div>
  <div class="contact">
    <p class="contact-name">Karim Ait Lounes</p>
    <p class="contact-role">Associé gérant</p>
    <p class="contact-line">
      <svg viewBox="0 0 12 12"><path d="M6 1a3.5 3.5 0 0 0-3.5 3.5C2.5 7.5 6 11 6 11s3.5-3.5 3.5-6.5A3.5 3.5 0 0 0 6 1zm0 5a1.4 1.4 0 1 1 0-2.8A1.4 1.4 0 0 1 6 6z" fill="var(--green-lime)"/></svg>
      <span>CP 7148, CH-1002 Lausanne<br>Switzerland</span>
    </p>
    <p class="contact-line">
      <svg viewBox="0 0 12 12"><path d="M3 1l2 2.5-1.2 1.3a6 6 0 0 0 3.4 3.4L8.5 7 11 9l-1.3 1.8C5.5 11 1 6.5 1.2 2.3z" fill="var(--green-lime)"/></svg>
      <span>+41 21 555 01 48</span>
    </p>
    <p class="contact-line">
      <svg viewBox="0 0 12 12"><rect x="1" y="2.5" width="10" height="7" rx="1" fill="var(--green-lime)"/><path d="M1.5 3l4.5 3.5L10.5 3" stroke="#fff" fill="none"/></svg>
      <span>kal@brookharlow.ch</span>
    </p>
    <p class="contact-line">
      <svg viewBox="0 0 12 12"><circle cx="6" cy="6" r="5" fill="var(--green-lime)"/><path d="M1 6h10M6 1c2 2.5 2 7.5 0 10M6 1c-2 2.5-2 7.5 0 10" stroke="#fff" stroke-width="0.7" fill="none"/></svg>
      <span>www.brookharlow.ch</span>
    </p>
  </div>
</section>

<section class="card card-back" aria-label="Business card back">
  <div class="brand">
    <span class="brand-name">Brook Harlow Supply &amp; Advisory sàrl</span>
  </div>
</section>

</body>
</html>
```